Ridgeway Framers Business Card

I'm looking for a business card design for a start-up Handyman/Construction Company. The organization will double as a ministry to the homeless, hoping to create job opportunity and training to the homeless, providing a pathway back to being "homed". I'm looking for a simple to "seeming" simple design. Open to all thoughts.

Industry/Entity Type

Ministry

Requirements
Must have
• Logo (Attached), Name, Phone, Email and Address. Note - "*Registered and Insured".

```html
<!DOCTYPE html>
<html lang="en">
<head>
<meta charset="utf-8">
<title>Ridgeway Framers Business Card</title>
<link href="https://fonts.googleapis.com/css2?family=Raleway:wght@400;500;700;800&display=swap" rel="stylesheet">
<style>
  :root {
    --navy: #223a5e;
    --purple: #8a2f93;
    --paper: #ffffff;
    --backdrop: #d9d9db;
    --panel-text: #ffffff;
    --panel-muted: #c9d3e2;
  }
  * { margin: 0; padding: 0; box-sizing: border-box; }
  html, body { width: 1200px; height: 900px; overflow: hidden; }
  body {
    background: var(--backdrop);
    font-family: "Raleway", sans-serif;
    position: relative;
  }
  .card {
    position: absolute;
    left: 250px;
    width: 700px;
    height: 400px;
    background: var(--paper);
    box-shadow: 0 6px 18px rgba(0,0,0,0.18);
    overflow: hidden;
  }
  .card--contact { top: 35px; }
  .card--brand { top: 465px; }

  .accent-bar { position: absolute; background: var(--navy); }

  /* contact face */
  .card--contact .accent-bar { left: 0; top: 95px; width: 36px; height: 170px; }
  .card--contact .wordmark {
    position: absolute; left: 50px; top: 158px;
    display: inline-block;
    color: var(--navy);
    font-weight: 800; font-size: 23px; letter-spacing: 0.5px; line-height: 1;
    white-space: nowrap;
  }
  .card--contact .wordmark small {
    display: block; font-size: 10px; font-weight: 500; letter-spacing: 0;
    text-align: right; margin-top: 4px;
  }
  .contact-panel {
    position: absolute; left: 350px; top: 80px; width: 350px; height: 164px;
    background: var(--navy);
    color: var(--panel-text);
    padding: 14px 22px;
  }
  .contact-panel .person-name { font-weight: 700; font-size: 18px; }
  .contact-panel .person-role { font-size: 8px; color: var(--panel-muted); margin-bottom: 12px; }
  .contact-panel .contact-line { font-size: 13px; line-height: 1.45; white-space: nowrap; }
  .contact-panel .contact-line b { font-weight: 400; display: inline-block; width: 18px; }
  .contact-panel .credential-note { font-size: 10px; color: var(--panel-muted); margin-top: 6px; }

  /* brand face */
  .card--brand .accent-bar--top { left: 0; top: 25px; width: 120px; height: 70px; }
  .card--brand .accent-bar--side { right: 0; top: 190px; width: 40px; height: 150px; }
  .brand-lockup {
    position: absolute; left: 0; right: 0; top: 110px; text-align: center;
  }
  .card--brand .wordmark {
    display: inline-block;
    color: var(--navy);
    font-weight: 800; font-size: 50px; letter-spacing: 1px; line-height: 1;
    white-space: nowrap;
  }
  .card--brand .wordmark small {
    display: block; font-size: 18px; font-weight: 500; letter-spacing: 0;
    margin-top: 6px; text-align: right;
  }
  .tagline {
    position: absolute; left: 0; right: 0; top: 262px; text-align: center;
    color: var(--purple); font-size: 19px;
  }
</style>
</head>
<body>
  <section class="card card--contact">
    <div class="accent-bar"></div>
    <div class="wordmark">RIDGEWAY FRAMERS<small>Builders, LLC</small></div>
    <div class="contact-panel">
      <div class="person-name">Daniel Marsh</div>
      <div class="person-role">General Manager</div>
      <div class="contact-line">12 Harbour Row, Sydney City, Australia</div>
      <div class="contact-line">50610</div>
      <div class="contact-line"><b>e.</b> hello@ridgewayframers.com</div>
      <div class="contact-line"><b>p.</b> +352 2871 3306</div>
      <div class="credential-note">*Registered and Insured</div>
    </div>
  </section>

  <section class="card card--brand">
    <div class="accent-bar accent-bar--top"></div>
    <div class="accent-bar accent-bar--side"></div>
    <div class="brand-lockup">
      <div class="wordmark">RIDGEWAY FRAMERS<small>Builders, LLC</small></div>
    </div>
    <p class="tagline">The organization will double as a ministry to the homeless</p>
  </section>
</body>
</html>
```